Veltharion Email Direct Marketing Campaign

This is an email campaign. The copy is attached. Also attached is our logo and business card. You can get some design ideas from those and our website (www.veltharion-example.com). But don't let those limit your ideas. We are open to suggestions. We want a great looking campaign that is in line with current clean design trends (including flat design) and marketing messaging.
Updates

Hi Designers. This is not a home page design or a logo redesign. This is the design of an email campaign which will arrive in people's inboxes as a promotion. Do not take wording from the website. All wording is in the text PDF attached. No coding is required. Thanks

Industry/Entity Type

Marketing

```html
<!DOCTYPE html>
<html lang="en">
<head>
<meta charset="utf-8">
<title>Veltharion Email Campaign</title>
<link href="https://fonts.googleapis.com/css2?family=Open+Sans:wght@400;600;700&display=swap" rel="stylesheet">
<style>
:root{
  --navy:#0f4a9a;
  --ink:#2a3a4a;
  --muted:#5a6f82;
  --red:#e8293a;
  --sky:#5bbfe6;
  --green:#a4cc2a;
  --green-dark:#7da617;
  --grey:#8d959c;
  --line:#d4d8dc;
  --tile:#3d4a57;
}
*{box-sizing:border-box;margin:0;padding:0}
html,body{width:1200px;height:3180px;overflow:hidden;background:#fff}
body{position:relative;font-family:'Open Sans',Arial,sans-serif;color:var(--ink)}
.abs{position:absolute}
.brand{font-weight:700;color:var(--navy);font-size:68px;letter-spacing:-1px;line-height:1}
.tagline{font-size:24px;color:var(--navy)}
.hero{left:0;top:170px;width:1200px;height:478px;background:linear-gradient(90deg,#7fa8b8 0%,#a9c7d3 35%,#d4e6ee 60%,#e9f3f7 100%)}
.hero-copy{left:695px;top:270px;width:440px;border-left:5px solid var(--navy);padding-left:16px}
.hero-copy h2{font-weight:400;color:var(--red);font-size:52px;line-height:1.1}
.hero-text{left:695px;top:364px;width:440px;font-size:25px;line-height:40px;color:#111}
.headline{left:0;top:690px;width:1200px;text-align:center;font-size:40px;line-height:56px;font-weight:600;color:var(--ink);white-space:nowrap;letter-spacing:-0.3px}
.subline{left:150px;top:764px;width:900px;text-align:center;font-size:27px;line-height:40px;color:var(--muted)}
.divider{left:40px;width:1125px;height:9px;background:repeating-linear-gradient(135deg,#c9ced3 0 2px,transparent 2px 6px)}
.section-title{font-size:42px;font-weight:400;color:var(--ink)}
.section-sub{font-size:20px;color:var(--muted)}
.service{width:270px}
.service svg{display:block}
.service h3{font-size:26px;font-weight:600;margin-top:26px;white-space:nowrap}
.service p{font-size:20px;line-height:32px;color:var(--muted);margin-top:20px}
.service .btn-row{text-align:center}
.btn{display:inline-flex;align-items:center;gap:10px;margin-top:28px;height:52px;padding:0 22px 0 14px;border-radius:6px;background:linear-gradient(#c8e45a,var(--green));border:2px solid var(--green-dark);font-size:20px;font-weight:600;color:#2e3a10}
.btn i{width:22px;height:22px;border-radius:50%;background:#3a4a20;display:inline-block}
.hub{width:346px}
.hub h3{font-size:28px;font-weight:400;display:flex;align-items:center;gap:14px;margin-left:4px}
.hub-card{margin-top:30px;height:235px;padding:12px;background:repeating-linear-gradient(135deg,#d6dade 0 2px,#fff 2px 6px);position:relative}
.hub-fill{width:100%;height:100%;display:flex;align-items:center;justify-content:center;font-size:40px;font-weight:700;color:#fff;text-align:center;line-height:1.1}
.ribbon{position:absolute;right:0;top:0;width:100px;height:100px;overflow:hidden}
.ribbon span{position:absolute;right:-38px;top:22px;width:160px;transform:rotate(45deg);background:#1c3e5c;color:#fff;font-size:16px;font-weight:700;text-align:center;line-height:32px}
.hub p{font-size:20px;line-height:33px;color:var(--muted);margin-top:22px;padding-left:8px}
.date{left:1024px;top:2262px;width:131px;height:155px;border-radius:10px;overflow:hidden;box-shadow:0 2px 4px rgba(0,0,0,.25)}
.date-day{height:108px;background:linear-gradient(#3b4a58,#16212b);color:#fff;font-size:66px;font-weight:600;text-align:center;line-height:108px}
.date-mon{height:47px;background:linear-gradient(#eceff1,#c7ccd0);font-size:21px;text-align:center;line-height:47px;color:#333}
.partners{left:50px;top:2670px;width:1110px;display:flex;justify-content:space-between;align-items:center}
.partners span{font-size:24px;font-weight:700;color:#7c848b}
.rule{left:26px;top:2795px;width:1150px;height:20px;background:var(--sky)}
.foot-brand{left:36px;top:2862px;font-size:54px;font-weight:700;color:#4a5560;letter-spacing:-1px}
.legal{right:40px;top:2870px;text-align:right;font-size:18px;line-height:30px;color:#a3aab0}
.legal u{color:#8c949a}
.foot-line{left:26px;top:2990px;width:1150px;height:2px;background:#e4e7ea}
.address{left:26px;top:3048px;font-size:21px;color:var(--ink)}
.contacts{left:26px;top:3086px;font-size:31px;font-weight:700;color:#2a6aa6;display:flex;align-items:center;gap:14px}
.social{left:742px;top:3054px;display:flex;gap:11px}
.social span{width:62px;height:64px;border-radius:4px;background:linear-gradient(#56636f,var(--tile));color:#fff;font-size:18px;font-weight:600;display:flex;align-items:center;justify-content:center}
</style>
</head>
<body>

<header>
  <div class="abs brand" style="left:40px;top:38px">Veltharion</div>
  <div class="abs tagline" style="left:755px;top:76px">content | community | commerce</div>
</header>

<section class="abs hero" role="img" aria-label="Photo of a smiling writer leaning on her arms in a bright office"></section>
<div class="abs hero-copy"><h2>Our Writers</h2></div>
<p class="abs hero-text">Our expert team of Australian writers, marketers and designers support you all the way</p>

<h1 class="abs headline">B2B media, marketing and technology solutions that work!</h1>
<p class="abs subline">Our targeted and measurable B2B media, marketing and technology solutions provide great results.</p>

<div class="abs divider" style="top:896px"></div>

<h2 class="abs section-title" style="left:46px;top:950px">Our Services</h2>
<p class="abs section-sub" style="left:54px;top:1028px">Vestibulum dapibus, mauris nec malesuada fames ac turpis rhoncus</p>

<div class="abs service" style="left:32px;top:1096px">
  <svg width="270" height="178" viewBox="0 0 270 178"><circle cx="131" cy="91" r="80" fill="#fff" stroke="#0f4a9a" stroke-width="10"/><circle cx="70" cy="28" r="17" fill="#a4cc2a" stroke="#34461a" stroke-width="3"/><text x="70" y="35" font-size="20" font-weight="700" text-anchor="middle" fill="#222" font-family="Open Sans,sans-serif">1</text><rect x="98" y="58" width="66" height="66" rx="10" fill="#e8293a"/><path d="M113 92l13 13 24-28" fill="none" stroke="#fff" stroke-width="8" stroke-linecap="round" stroke-linejoin="round"/></svg>
  <h3>Directory Advertising</h3>
  <p>Vestibulum dapibus, mauris nec malesuada fames turpis velit, rhoncus dolor fringilla.</p>
  <div class="btn-row"><span class="btn"><i></i>View</span></div>
</div>
<div class="abs service" style="left:322px;top:1096px">
  <svg width="270" height="178" viewBox="0 0 270 178"><circle cx="131" cy="91" r="80" fill="#fff" stroke="#0f4a9a" stroke-width="10"/><circle cx="70" cy="28" r="17" fill="#a4cc2a" stroke="#34461a" stroke-width="3"/><text x="70" y="35" font-size="20" font-weight="700" text-anchor="middle" fill="#222" font-family="Open Sans,sans-serif">2</text><g fill="none" stroke="#e8293a" stroke-width="6"><circle cx="131" cy="91" r="36"/><ellipse cx="131" cy="91" rx="15" ry="36"/><path d="M95 91h72M101 73h60M101 109h60M131 55v72"/></g></svg>
  <h3>Website Packages</h3>
  <p>Vestibulum dapibus, mauris nec malesuada fames turpis velit, rhoncus dolor fringilla.</p>
  <div class="btn-row"><span class="btn"><i></i>View</span></div>
</div>
<div class="abs service" style="left:612px;top:1096px">
  <svg width="270" height="178" viewBox="0 0 270 178"><circle cx="131" cy="91" r="80" fill="#fff" stroke="#0f4a9a" stroke-width="10"/><circle cx="70" cy="28" r="17" fill="#a4cc2a" stroke="#34461a" stroke-width="3"/><text x="70" y="35" font-size="20" font-weight="700" text-anchor="middle" fill="#222" font-family="Open Sans,sans-serif">3</text><g fill="none" stroke="#e8293a" stroke-width="5"><rect x="96" y="64" width="52" height="42" transform="rotate(-14 122 85)"/><rect x="112" y="78" width="56" height="44" fill="#fff" transform="rotate(8 140 100)"/></g><path d="M120 114l12-14 10 10 8-6 12 12z" fill="#e8293a"/><circle cx="150" cy="92" r="5" fill="#e8293a"/></svg>
  <h3>Display Advertising</h3>
  <p>Vestibulum dapibus, mauris nec malesuada fames turpis velit, rhoncus dolor fringilla.</p>
  <div class="btn-row"><span class="btn"><i></i>View</span></div>
</div>
<div class="abs service" style="left:902px;top:1096px">
  <svg width="270" height="178" viewBox="0 0 270 178"><circle cx="131" cy="91" r="80" fill="#fff" stroke="#0f4a9a" stroke-width="10"/><circle cx="70" cy="28" r="17" fill="#a4cc2a" stroke="#34461a" stroke-width="3"/><text x="70" y="35" font-size="20" font-weight="700" text-anchor="middle" fill="#222" font-family="Open Sans,sans-serif">4</text><path d="M93 84h76v40H93z" fill="#e8293a"/><path d="M93 84l38 24 38-24" fill="none" stroke="#fff" stroke-width="4"/><path d="M123 52h16v22h12l-20 20-20-20h12z" fill="#e8293a"/></svg>
  <h3>Targeted Email Lists</h3>
  <p>Vestibulum dapibus, mauris nec malesuada fames turpis velit, rhoncus dolor fringilla.</p>
  <div class="btn-row"><span class="btn"><i></i>View</span></div>
</div>

<div class="abs hub" style="left:36px;top:1676px">
  <h3><svg width="28" height="28" viewBox="0 0 28 28"><circle cx="11" cy="11" r="8" fill="none" stroke="#1d6fb8" stroke-width="3.5"/><path d="M17 17l8 8" stroke="#1d6fb8" stroke-width="4" stroke-linecap="round"/></svg>Plantwise Search</h3>
  <div class="hub-card"><div class="hub-fill" style="background:linear-gradient(135deg,#ff4a55,#e8283a)" role="img" aria-label="Plantwise Search listing artwork">Plantwise Search</div><div class="ribbon"><span>NEW!</span></div></div>
  <p>For industry professionals in manufacturing, industrial, mining, construction, safety, infrastructure and distribution.</p>
</div>
<div class="abs hub" style="left:424px;top:1676px">
  <h3><svg width="30" height="26" viewBox="0 0 30 26"><circle cx="10" cy="7" r="6" fill="#1d6fb8"/><circle cx="22" cy="8" r="5" fill="#1d6fb8"/><path d="M0 24c0-8 4-11 10-11s10 3 10 11zM19 24c0-5-1-8-3-10 2-1 4-1 6-1 5 0 8 3 8 11z" fill="#1d6fb8"/></svg>Clinora Search</h3>
  <div class="hub-card"><div class="hub-fill" style="background:linear-gradient(135deg,#4c86dc,#2a5eb8)" role="img" aria-label="Clinora Search listing artwork">Clinora Search</div><div class="ribbon"><span>NEW!</span></div></div>
  <p>For healthcare professionals in hospitals, medical practices, dental rooms, aged care facilities, surgeries and laboratories.</p>
</div>
<div class="abs hub" style="left:812px;top:1676px">
  <h3><svg width="28" height="28" viewBox="0 0 28 28"><rect x="2" y="10" width="24" height="7" fill="#1d6fb8"/><rect x="4" y="17" width="20" height="10" fill="#1d6fb8"/><rect x="12" y="10" width="4" height="17" fill="#fff"/><path d="M14 10c-3-8-10-6-7 0M14 10c3-8 10-6 7 0" fill="none" stroke="#1d6fb8" stroke-width="3"/></svg>Venuely Hub</h3>
  <div class="hub-card"><div class="hub-fill" style="background:linear-gradient(135deg,#b6d93a,#8cbf1c)" role="img" aria-label="Venuely Hub listing artwork">Venuely Hub</div><div class="ribbon"><span>NEW!</span></div></div>
  <p>For hospitality professionals in hotels, clubs, pubs, restaurants, events facilities and catering companies.</p>
</div>

<div class="abs divider" style="top:2206px"></div>

<h2 class="abs section-title" style="left:44px;top:2250px;font-size:44px">Industrial marketing 101</h2>
<p class="abs" style="left:44px;top:2318px;width:920px;font-size:22px;line-height:33px;color:var(--muted)">Phasellus fermentum in, dolor. Pellentesque facilisis. Nulla imperdiet sit amet magna. Vestibulum dapibus, mauris nec malesuada fames ac turpis velit, rhoncus eu, luctus et interdum adipiscing wisi.</p>
<div class="abs date"><div class="date-day">25</div><div class="date-mon">Aug</div></div>

<div class="abs divider" style="top:2490px"></div>

<h2 class="abs section-title" style="left:40px;top:2518px">Trusted By</h2>
<p class="abs" style="left:42px;top:2588px;font-size:20px;color:var(--muted)">We Are Trusted By Thousand's of Successfull Brands</p>
<div class="abs partners">
  <span>Korvan</span><span>Meriden Care</span><span>kinetiq supply</span><span>Ember Grill</span><span>Tarro</span><span>Quell Drive</span><span>baylift</span><span>Vantor</span>
</div>

<div class="abs rule"></div>

<footer>
  <div class="abs foot-brand">Veltharion</div>
  <div class="abs legal">Copyright © 2014 Veltharion<br>You are currently signed up to Veltharion newsletters. <u>To unsubscribe click here</u></div>
  <div class="abs foot-line"></div>
  <p class="abs address">Level 4, 22 Marlow Lane, Eastbrook, Sydney, NSW 2010, Australia</p>
  <div class="abs contacts">
    <svg width="22" height="32" viewBox="0 0 22 32"><rect x="2" y="1" width="18" height="30" rx="3" fill="none" stroke="#2a3a4a" stroke-width="3"/><path d="M8 26h6" stroke="#2a3a4a" stroke-width="3"/></svg>
    <span>1300 555 019</span>
    <svg width="34" height="24" viewBox="0 0 34 24" style="margin-left:18px"><rect x="2" y="2" width="30" height="20" fill="none" stroke="#2a3a4a" stroke-width="3"/><path d="M2 2l15 12L32 2" fill="none" stroke="#2a3a4a" stroke-width="3"/></svg>
    <span>(+61 2) 5550 1234</span>
  </div>
  <div class="abs social"><span>Kiv</span><span>Orn</span><span>Dal</span><span>Pex</span><span>Wim</span><span>Fao</span></div>
</footer>

</body>
</html>
```